Vereins Website
Zielgruppe
Webiste für den Verein 'Katzenhain Oberlau' (details siehe Anhang).
Ziel der Website:
- Sponsoren finden
- Vereinsmitglieder finden & Interessen bündeln.
Aufgabenstellung
Die Webiste sollt aufgeräumt, übersichtlich und freundlich wirken.

```html
<!DOCTYPE html>
<html lang="de">
<head>
<meta charset="utf-8">
<title>Verein Katzenhain Oberlau</title>
<link href="https://fonts.googleapis.com/css2?family=Montserrat:wght@400;500;600;700&family=Roboto:wght@400;500;700&display=swap" rel="stylesheet">
<style>
:root{
  --orange:#f4a73b;
  --text:#555;
  --dark:#333;
  --cream:#fbf2ec;
  --footer:#4a3b33;
  --field:#c9c9c9;
}
*{box-sizing:border-box;margin:0;padding:0}
html,body{width:1200px;height:2989px;overflow:hidden;background:#fff}
body{position:relative;font-family:'Montserrat',sans-serif;color:var(--text)}
.abs{position:absolute}
.site-header{position:absolute;left:0;top:0;width:1200px;height:62px;background:#fff;border-bottom:1px solid #eee}
.brand{position:absolute;left:258px;top:14px;display:flex;align-items:center;gap:8px;font-size:11px;font-weight:700;color:var(--dark);line-height:1.1}
.brand-dot{width:26px;height:26px;border-radius:50%;background:var(--orange)}
.nav{position:absolute;top:27px;font-size:11px;font-weight:500;color:var(--dark);letter-spacing:.3px}
.hero{position:absolute;left:0;top:62px;width:1200px;height:515px;background:linear-gradient(180deg,#a9b98a 0%,#8ea466 45%,#6f8f3f 100%)}
.hero-title{position:absolute;left:0;width:1200px;top:180px;text-align:center;font-weight:700;font-size:43px;line-height:44px;color:#fff;text-shadow:0 2px 6px rgba(0,0,0,.35)}
.btn{position:absolute;background:var(--orange);color:#fff;font-weight:600;text-align:center;text-transform:uppercase}
.hero .btn{height:34px;line-height:34px;font-size:15px;top:309px}
.section-title{position:absolute;left:0;width:1200px;text-align:center;font-family:'Roboto',sans-serif;font-weight:500;font-size:28px;color:var(--dark);display:flex;justify-content:center;align-items:center;gap:10px}
.intro-text{position:absolute;left:258px;top:731px;width:689px;font-size:15px;line-height:17.7px;text-align:justify}
.photo{position:absolute;left:0;width:1200px}
.kicker{position:absolute;font-size:12px;color:var(--orange);text-transform:uppercase}
.body-sm{position:absolute;font-size:12.5px;line-height:18.5px;text-align:justify}
.field{position:absolute;height:28px;border:1px solid var(--field);font-size:10px;color:#999;padding:7px 9px;font-family:Arial,sans-serif}
.form .btn{height:27px;line-height:27px;font-size:11px;font-weight:500}
.sponsors{position:absolute;left:0;top:1816px;width:1200px;height:302px;background:var(--cream)}
.logo-tile{position:absolute;top:153px;height:84px;background:#fff;display:flex;align-items:center;justify-content:center;font-size:14px;font-weight:600;color:var(--dark)}
.account{position:absolute;left:405px;top:2270px;font-size:18px;line-height:21px;color:var(--dark)}
.account b{font-weight:700}
.pay{position:absolute;top:2367px;height:38px;display:flex;align-items:center;justify-content:center;font-size:13px;font-weight:600;color:var(--dark)}
.band{position:absolute;left:0;top:2483px;width:1200px;height:257px;background:linear-gradient(90deg,#6b4a2e,#8c6340 40%,#a67b55 70%,#7a8a4a)}
.band-title{position:absolute;left:0;width:1200px;top:112px;text-align:center;font-weight:700;font-size:29px;color:#fff;text-shadow:0 2px 6px rgba(0,0,0,.4)}
.footer{position:absolute;left:0;top:2953px;width:1200px;height:36px;background:var(--footer);color:#fff;font-size:11px;text-align:center;line-height:36px}
</style>
</head>
<body>
<svg width="0" height="0" style="position:absolute">
  <defs>
    <symbol id="bone" viewBox="0 0 48 28">
      <path d="M10 4a6 6 0 0 1 6 6h16a6 6 0 1 1 6 6 6 6 0 1 1-6 6H16a6 6 0 1 1-6-6 6 6 0 1 1 0-12z" fill="none" stroke="#f4a73b" stroke-width="4" stroke-linejoin="round"/>
    </symbol>
  </defs>
</svg>

<header class="site-header">
  <div class="brand"><span class="brand-dot"></span><span>Verein<br>Katzenhain<br>Oberlau</span></div>
  <span class="nav" style="left:718px">MITGLIED</span>
  <span class="nav" style="left:799px">SPONSOR</span>
  <span class="nav" style="left:882px">KONTAKT</span>
</header>

<section class="hero" role="img" aria-label="Foto: Hund rennt über eine sonnige Wiese vor Bäumen">
  <h1 class="hero-title">Lorem ipsum dolor sit amet mit<br>Verein Katzenhain Oberlau</h1>
  <span class="btn" style="left:390px;width:183px">Mitglied werden</span>
  <span class="btn" style="left:630px;width:187px">Sponsor werden</span>
</section>

<h2 class="section-title" style="top:660px"><svg width="46" height="28"><use href="#bone"/></svg>Verein Katzenhain Oberlau</h2>
<div class="intro-text">
  <p>Nach dem Vorbild von Birkach möchten wir in Oberlau eine eingezäunte Hundespielwiese auf die Beine stellen und damit das Wohlergehen der Hunde fördern.Auf der eingezäunten Wiese können die Hunde ohne Leinenzwang spielen, sich austoben und sozialisieren.Gleichzeitig schafft dies einen Raum, in dem sich die Hundehalter treffen und austauschen können.</p>
  <p style="margin-top:17px">Ein Begegnungsort für die ganze Region, von dem alle profitieren.</p>
</div>

<div class="photo" style="top:924px;height:398px;background:linear-gradient(90deg,#b9c0c4 0%,#9aa5ab 30%,#3e4f70 50%,#d9c9a6 70%,#8fb35a 100%)" role="img" aria-label="Foto: Person streichelt einen Golden Retriever auf der Wiese"></div>

<h2 class="section-title" style="top:1437px"><svg width="46" height="28"><use href="#bone"/></svg>Werden Sie Vereinsmitglied</h2>
<span class="kicker" style="left:66px;top:1530px">Projekt unterstützen und Vereinsmitglied werden</span>
<p class="body-sm" style="left:66px;top:1555px;width:362px">Lorem ipsum dolor sit amet, eu sed nulla imperdiet complectitur, dico philosophia eu vel, dicunt maluisset imperdiet et eos. At usu verterem partiendo consetetur, id nullam laboramus nec. Et paulo nobis integre sit, qui ludus option periculis id.</p>
<p class="body-sm" style="left:66px;top:1665px;width:362px;font-weight:600;color:#222">Eine Vereinsmitgliedschaft ist derzeit noch kostenlos.<br>Sie unterstützen den Verein damit ideell.</p>

<div class="form">
  <span class="kicker" style="left:588px;top:1530px">Anmeldeformular</span>
  <div class="field" style="left:588px;top:1560px;width:257px">Name</div>
  <div class="field" style="left:874px;top:1560px;width:257px">Strasse / Nr.</div>
  <div class="field" style="left:588px;top:1608px;width:257px">Vorname</div>
  <div class="field" style="left:874px;top:1608px;width:59px">PLZ</div>
  <div class="field" style="left:588px;top:1657px;width:257px">E-Mail Adresse</div>
  <div class="field" style="left:874px;top:1657px;width:257px">Ort</div>
  <span class="btn" style="left:588px;top:1706px;width:73px">Senden</span>
</div>

<section class="sponsors">
  <h2 class="section-title" style="top:46px"><svg width="46" height="28"><use href="#bone"/></svg>Werden Sie Sponsor</h2>
  <span class="kicker" style="left:0;width:1262px;text-align:center;top:90px">Helfen Sie uns dieses Projekt zu verwirklichen</span>
  <div class="logo-tile" style="left:96px;width:126px">Pfotenküche</div>
  <div class="logo-tile" style="left:326px;width:95px;background:var(--orange);font-size:11px;font-weight:500;text-align:center;line-height:13px">HIER KÖNNTE<br>IHR LOGO<br>STEHEN</div>
  <div class="logo-tile" style="left:536px;width:106px">Schalenglück</div>
  <div class="logo-tile" style="left:754px;width:126px">Wedelwohl</div>
  <div class="logo-tile" style="left:983px;width:126px;top:168px;height:55px">Fellkrone</div>
</section>

<h2 class="section-title" style="top:2182px">
  <svg width="48" height="30" viewBox="0 0 48 30"><rect x="2" y="2" width="44" height="26" fill="none" stroke="#f4a73b" stroke-width="3"/><rect x="7" y="7" width="34" height="16" fill="#f4a73b"/><circle cx="24" cy="15" r="5" fill="#fff"/></svg>Spenden</h2>
<div class="account">
  <b>SPENDENKONTO:</b> KATZENHAIN OBERLAU<br>
  <b>IBAN:</b> 98 00000 00000 00000 9<br>
  <b>BIC:</b> 6553873
</div>
<div class="pay" style="left:399px;width:40px;background:#111;color:#fff;font-size:8px">Zahl&shy;punkt</div>
<div class="pay" style="left:460px;width:129px;background:#ffd200">Kontoblick</div>
<div class="pay" style="left:604px;width:64px">Netzgeld</div>
<div class="pay" style="left:681px;width:125px;top:2370px;height:32px;background:var(--orange);font-size:9px;font-weight:500">EINZAHLUNGSSCHEIN</div>

<section class="band" role="img" aria-label="Foto: Hände halten liebevoll einen braunen Hund im Gras">
  <h2 class="band-title">Wir freuen uns auf Ihre Anregungen &amp; Ideen</h2>
</section>

<div class="form">
  <div class="field" style="left:287px;top:2791px;width:308px">Name</div>
  <div class="field" style="left:287px;top:2826px;width:308px">E-Mail Adresse</div>
  <div class="field" style="left:639px;top:2791px;width:308px;height:63px">Ihr Text</div>
  <div class="abs" style="left:287px;top:2865px;font-size:9.5px;font-family:Arial,sans-serif;display:flex;align-items:center;gap:9px"><span style="width:9px;height:9px;border:1px solid #999"></span>Kopie an meine E-Mail Adresse</div>
  <span class="btn" style="left:287px;top:2893px;width:67px">Senden</span>
</div>

<footer class="footer">info@katzenhain-oberlau.ch</footer>
</body>
</html>
```